Broschüre für Baumanagement
Zielgruppe
Baumanagement
Wir liefern von der Planung, über die notwendigen Handwerksfirmen langjährige Partner, Bauleitung alle notwenidgen Partner
Wir betreuen seit jahren Kunden aus dem Immobilienwesen, Handel usw.
Ein Ansprechpartner vond er Planung bis zur Übergabe
Aufgabenstellung
DIN A4, 2 Seiten, Modern, Fakten, Gerne nur in schwarz und weiss halten

```html
<!DOCTYPE html>
<html lang="de">
<head>
<meta charset="utf-8">
<title>Baumanagement – Broschüre</title>
<link rel="stylesheet" href="https://fonts.googleapis.com/css2?family=Open+Sans:wght@400;600;700&family=Roboto:wght@700&family=Roboto+Slab:wght@300&display=swap">
<style>
  :root {
    --backdrop: #c6c6c6;
    --paper: #ffffff;
    --ink: #000000;
    --ink-soft: #1c1c1c;
    --reverse: #ffffff;
    --logo-box: #f2f2f2;
    --sky-top: #c3d6e3;
    --sky-mid: #dfe8ee;
    --facade: #eef0f1;
    --facade-shade: #b9c3ca;
  }
  * { box-sizing: border-box; margin: 0; padding: 0; }
  html, body {
    width: 1200px; height: 785px; overflow: hidden;
    background: var(--backdrop);
  }
  body { position: relative; font-family: "Open Sans", sans-serif; color: var(--ink); }

  .page {
    position: absolute; top: 62px;
    width: 467px; height: 660px;
    background: var(--paper);
    overflow: hidden;
    box-shadow: 0 6px 14px rgba(0,0,0,.25);
  }
  .page--front { left: 75px; }
  .page--back  { left: 658px; }

  .photo {
    position: absolute;
    background: linear-gradient(160deg, var(--sky-top) 0%, var(--sky-mid) 30%, var(--facade) 55%, var(--facade-shade) 100%);
  }

  /* Front page */
  .front__header {
    position: absolute; left: 0; top: 0; width: 100%; height: 118px;
    background: var(--paper); z-index: 2;
  }
  .front__photo { left: 0; top: 118px; width: 100%; bottom: 0; }
  .logo {
    position: absolute; left: 30px; top: 36px; width: 160px; height: 66px;
    background: var(--logo-box);
    display: flex; align-items: center; justify-content: center; gap: 8px;
  }
  .logo__mark { width: 12px; height: 12px; background: var(--ink); }
  .logo__name {
    font-family: "Open Sans", sans-serif; font-weight: 700;
    font-size: 12px; letter-spacing: .3px; color: var(--ink);
  }
  .contact {
    position: absolute; left: 300px; top: 40px;
    font-size: 7.4px; line-height: 11.5px; color: var(--ink-soft);
  }
  .contact-person {
    position: absolute; left: 300px; top: 132px; z-index: 2;
    line-height: 1.3; color: var(--ink-soft);
  }
  .contact-person__label { font-size: 8.5px; }
  .contact-person__name { font-size: 10px; font-weight: 700; }
  .contact-person__role { font-size: 6.5px; }

  .title-band {
    position: absolute; left: 0; top: 490px; width: 100%; height: 90px;
    background: var(--ink); z-index: 2;
    display: flex; align-items: center; justify-content: center;
  }
  .title-band__text {
    font-family: "Roboto Slab", serif; font-weight: 300;
    font-size: 40px; letter-spacing: 1px; color: var(--reverse);
  }
  .front__claim {
    position: absolute; left: 30px; top: 592px; z-index: 2;
    font-family: "Roboto", sans-serif; font-weight: 700; font-size: 12.5px;
  }
  .front__intro {
    position: absolute; left: 30px; top: 614px; z-index: 2;
    font-size: 9.5px; color: var(--ink-soft);
  }

  /* Back page */
  .back__photo { right: 0; top: 0; width: 124px; height: 100%; }
  .back__panel {
    position: absolute; left: 0; top: 0; width: 343px; height: 100%;
    background: var(--ink); color: var(--reverse);
  }
  .heading { position: absolute; left: 50px; top: 140px; width: 240px; }
  .heading__kicker { font-weight: 700; font-size: 12px; }
  .heading__rule-top { position: absolute; left: 44px; top: 8px; width: 196px; height: 2px; background: var(--reverse); }
  .heading__main {
    font-family: "Roboto Slab", serif; font-weight: 300;
    font-size: 33px; line-height: 1; margin-top: 2px; letter-spacing: .5px;
  }
  .heading__rule-bottom { width: 76px; height: 2px; background: var(--reverse); margin-top: 8px; }
  .heading__sub {
    position: absolute; right: 0; top: 62px;
    font-weight: 700; font-size: 11.5px; letter-spacing: .4px;
  }
  .back__text {
    position: absolute; left: 50px; top: 300px; width: 270px;
    font-weight: 600; font-size: 16px; line-height: 16px;
  }
  .signature {
    position: absolute; right: 26px; top: 510px; text-align: right; line-height: 1.2;
  }
  .signature__name { font-weight: 700; font-size: 9.5px; }
  .signature__role { font-size: 6.5px; }
</style>
</head>
<body>

<section class="page page--front">
  <header class="front__header">
    <div class="logo">
      <span class="logo__mark"></span>
      <span class="logo__name">KAROVA GRUPPE</span>
    </div>
    <address class="contact" style="font-style:normal">
      Lindenweg 8, 12345 Musterort<br>
      Phone: 0987 6543 210<br>
      E-mail: kontakt@karova-bau.de<br>
      Web : www.karova-bau.de
    </address>
  </header>

  <div class="photo front__photo" role="img" aria-label="Foto: moderner weißer Wohnbau mit auskragenden Geschossen vor hellblauem Himmel"></div>

  <div class="contact-person">
    <p class="contact-person__label">Ihr Ansprechpartner</p>
    <p class="contact-person__name">Jonas Brandt</p>
    <p class="contact-person__role">General Manager</p>
  </div>

  <div class="title-band"><h1 class="title-band__text">BAUMANAGEMENT</h1></div>
  <p class="front__claim">Ein Ansprechpartner von der Planung bis zur Übergabe</p>
  <p class="front__intro">Wir betreuen seit jahren Kunden aus dem Immobilienwesen, Handel.</p>
</section>

<section class="page page--back">
  <div class="photo back__photo" role="img" aria-label="Foto: Ausschnitt des weißen Wohnbaus vor hellblauem Himmel"></div>
  <div class="back__panel">
    <div class="heading">
      <span class="heading__kicker">BAU</span>
      <span class="heading__rule-top"></span>
      <h2 class="heading__main">ARCHITEKTUR</h2>
      <div class="heading__rule-bottom"></div>
      <p class="heading__sub">WIR PLANEN FÜR SIE</p>
    </div>
    <p class="back__text">
      Wir liefern von der Planung,<br>
      über die notwendigen<br>
      Handwerksfirmen<br>
      langjährige Partner,<br>
      Bauleitung alle notwenidgen<br>
      Partner
    </p>
    <div class="signature">
      <p class="signature__name">Jonas Brandt</p>
      <p class="signature__role">General Manager</p>
    </div>
  </div>
</section>

</body>
</html>
```